IT Network Consultancy - Brochure

m2 relays is a IT network consultancy based in London. We're looking for a smart, modern and professional brochure in A4 format. Our website is here: www.m2relays.co.uk. We likely will require the brochure in two formats:

PDF / Scroll Down (The most common distribution of the brochure will be PDF, which will scroll down page after page):

Page 1 - Front page
Page 2 - Portrait / scroll down
Page 3 - Portrait / scroll down
Page 4 - Portrait / scroll down
Page 5 - Portrait / scroll down
Page 6 - Back page

Side by Side / Professionally Printed:

Page 1 - Front page
Page 2/3 - Side by side
Page 4/5 - Side by side
Page 6 - Back page
Updates

Please note - I made a number of changes to the design brief after initially submitting it.

I have also increased the first prize budget from £150 to £200 (US $327)

Images may be used - no pictures of people though or anything too bright...

Reason: We're extending the deadline as we haven't received as many designs as we'd liked (one so far!)

Following a question from another designer:

We're a technology consultancy, not a technology company.  We don't need any futuristic graphics, just something that looks clean and professional.  Almost along the lines of financial services but not to traditional.

Target Market(s)

Large enterprise / global companies / corporates

Industry/Entity Type

Distribution

Requirements
Must have
• Incorporate our logo - which is attached to the project. They are in AI format (can be opened in Inkscape).

Initially the brochure is to be used specifically for our company profile / fact sheet (see attached PPT for text).

We would like to have a template we can also use for future documents.

Fonts should be simple.
Nice to have
• The project does not have to conform to the colour of our website but this should give you inspiration of the style we like.

A way to incorporate the design into MS PowerPoint, i.e. a template for corporate presentations.
Should not have
• Bright colours.

```html
<!DOCTYPE html>
<html lang="en">
<head>
<meta charset="utf-8">
<title>M2 Relays – Company Profile Brochure</title>
<link rel="stylesheet" href="https://fonts.googleapis.com/css2?family=Arimo:wght@400;700&display=swap">
<style>
  :root {
    --canvas: #ffffff;
    --panel-grey: #b9c0c9;
    --tab-grey: #9aa1aa;
    --tab-grey-light: #c9ced5;
    --header-slate: #414d58;
    --text-dark: #4a5058;
    --text-body: #3b3f44;
    --logo-grey: #6f767e;
    --photo-deep: #4e6276;
    --photo-mid: #8fa3b6;
    --photo-light: #dfe7ee;
    --page-white: #ffffff;
    --page-edge: #d5d9de;
  }
  * { box-sizing: border-box; margin: 0; padding: 0; }
  html, body {
    width: 1200px; height: 900px; overflow: hidden;
    background: var(--canvas);
    font-family: "Arimo", Arial, sans-serif;
  }
  .spread { position: relative; width: 1200px; height: 900px; }

  .page {
    position: absolute;
    background: var(--page-white);
    border: 1px solid var(--page-edge);
    overflow: hidden;
  }

  /* ---------- Front cover ---------- */
  .cover { left: 22px; top: 40px; width: 572px; height: 810px; }
  .cover__panel {
    position: absolute; left: 0; top: 0; width: 330px; height: 100%;
    background: var(--panel-grey);
  }
  .cover__photo {
    position: absolute; left: 330px; top: 0; right: 0; bottom: 0;
    background:
      radial-gradient(ellipse at 40% 60%, var(--photo-light) 0%, transparent 45%),
      linear-gradient(160deg, var(--photo-mid) 0%, var(--photo-deep) 55%, #2f3d4a 100%);
  }
  .logo-box {
    position: absolute; background: var(--page-white);
    display: flex; align-items: center; justify-content: center;
  }
  .cover .logo-box {
    left: 32px; top: 48px; width: 236px; height: 146px;
    border-radius: 0 28px 0 28px;
  }
  .logo-name {
    font-weight: 400; color: var(--logo-grey);
    letter-spacing: 0.06em; text-transform: uppercase; white-space: nowrap;
  }
  .cover .logo-name { font-size: 30px; }

  .service-tabs {
    position: absolute; left: 350px; top: 30px; list-style: none;
  }
  .service-tabs li {
    width: 210px; height: 36px; margin-bottom: 16px;
    background: var(--tab-grey-light);
    border-radius: 8px 8px 8px 8px;
    color: var(--text-dark); font-size: 17px;
    padding: 8px 0 0 14px;
    box-shadow: 0 1px 2px rgba(0,0,0,.25);
  }

  .section-tab {
    display: inline-block; background: var(--tab-grey);
    color: var(--page-white); font-size: 14px;
    border-radius: 0 10px 0 10px;
  }
  .cover .section-tab {
    position: absolute; left: 54px; top: 340px;
    width: 210px; height: 26px; padding: 5px 12px;
  }
  .cover__intro {
    position: absolute; left: 54px; top: 376px; width: 262px;
    font-size: 17px; line-height: 1.3; color: var(--text-dark);
  }

  /* ---------- Inside page ---------- */
  .inside { left: 612px; top: 110px; width: 560px; height: 770px; }
  .inside__header {
    height: 132px; background: var(--header-slate); position: relative;
  }
  .inside .logo-box {
    left: 40px; top: 40px; width: 232px; height: 56px;
    border-radius: 0 16px 0 16px;
  }
  .inside .logo-name { font-size: 24px; }

  .inside__body { padding: 20px 48px 0 62px; color: var(--text-body); }
  .inside__body .section-tab {
    width: 200px; height: 28px; padding: 6px 14px; font-size: 14px;
    margin: 14px 0 12px;
  }
  .inside__body p { font-size: 10.5px; line-height: 1.45; }
  .ticks { list-style: none; font-size: 10.5px; line-height: 1.45; margin-top: 2px; }
  .ticks li { padding-left: 10px; position: relative; }
  .ticks li::before {
    content: "\2713"; position: absolute; left: 0; top: 0;
    font-size: 8px; color: var(--tab-grey);
  }
  .page-number {
    position: absolute; left: 0; bottom: 0; width: 34px; height: 28px;
    background: var(--tab-grey-light); color: var(--text-dark);
    font-size: 11px; padding: 8px 0 0 12px; border-radius: 0 12px 0 0;
  }
</style>
</head>
<body>
<main class="spread">

  <section class="page cover">
    <div class="cover__panel"></div>
    <div class="cover__photo" role="img" aria-label="Close-up photograph of bundled network patch cables and connectors in cool blue-grey tones"></div>

    <div class="logo-box"><span class="logo-name">m2 relays</span></div>

    <ul class="service-tabs">
      <li>architecture</li>
      <li>design</li>
      <li>implementation</li>
      <li>network</li>
      <li>audit</li>
      <li>team support</li>
    </ul>

    <span class="section-tab">Company Profile</span>
    <p class="cover__intro">M2 Relays is a London based consultancy specialising in IT networking and network security solutions. Our commitment is to build strong and lasting relationships with our customers. We aim to understand our customers’ business goals, business principles and strategic drivers to ensure that our delivery is aligned and relevant.</p>
  </section>

  <section class="page inside">
    <header class="inside__header">
      <div class="logo-box"><span class="logo-name">m2 relays</span></div>
    </header>

    <div class="inside__body">
      <span class="section-tab">Values</span>
      <p>M2 is founded on the following core values:</p>
      <ul class="ticks">
        <li>Integrity first</li>
        <li>Dedication to our customer’s success</li>
        <li>Driven by technical leadership</li>
      </ul>

      <span class="section-tab">Mission Statement</span>
      <p>M2’s mission is to by exceeding all expectations in technical knowledge, professional standards and delivery.</p>

      <span class="section-tab">History</span>
      <p>While M2 is a young organisation, our founders have extensive experience. From consultancy services and project delivery, to strategy and architectural guidance, we have:</p>
      <ul class="ticks">
        <li>Delivered large and complex projects on time, on budget and to specification</li>
        <li>Developed scalable, reliable and integrated network architectures</li>
        <li>Produced technology roadmaps, defined strategic frameworks, and managed technology integrations</li>
        <li>Optimised infrastructure and delivered operational efficiency improvements</li>
        <li>Created innovative, simple and elegant solutions</li>
      </ul>
    </div>

    <span class="page-number">2</span>
  </section>

</main>
</body>
</html>
```